Professional Modern Website Design

We are a premium IT services provider to the financial industry based in London. Our company is called Velmar our current holding page is www.velmar.co.uk. We require a new website to match our new corporate identity. This project is for the design phase only. Development will be handled in-house. I have attached examples of wire frames we have developed (although open to suggestions for improvement) Our brand document that should demonstrate current brand, inc how we communicate to potential clients and finally mostly completed web-content.
We are looking for designers that can create something that sets us apart from our competitors.
Target Market(s)
IT Decision makers in Finance companies such as; hedge funds, private investment banks etc
Industry/Entity Type
Financial
Number of Pages Required
5+ page
Requirements
Must have
- hexagon elements in the design, unique design.
Nice to have
- Blog and social media feeds
Should not have
- Should not resemble a downloaded template

```html
<!DOCTYPE html>
<html lang="en">
<head>
<meta charset="utf-8">
<title>Velmar – IT Integration for Finance</title>
<link rel="stylesheet" href="https://fonts.googleapis.com/css2?family=Arimo:wght@400;700&display=swap">
<style>
:root{
  --orange:#f26a1b;
  --orange-light:#ff9a4a;
  --orange-dark:#d9520a;
  --ink:#333;
  --muted:#555;
  --panel:#f2f2f2;
  --line:#d6d6d6;
  --band:#e4e4e4;
  --footer:#3a3a3a;
  --footer-deep:#111;
  --white:#fff;
}
*{box-sizing:border-box;margin:0;padding:0}
html,body{width:768px;height:1200px;overflow:hidden;background:var(--white)}
body{font-family:"Arimo",Arial,sans-serif;color:var(--ink);position:relative}
.page{position:relative;width:768px;height:1200px;overflow:hidden}
.abs{position:absolute}

/* header */
.brand{left:150px;top:30px;display:flex;align-items:center;gap:8px}
.brand-mark{width:22px;height:22px;background:var(--orange)}
.brand-name{font-size:24px;font-weight:700;color:var(--orange)}
.search{left:334px;top:47px;display:flex;align-items:center;gap:5px}
.search input{width:96px;height:17px;border:1px solid #bbb;border-radius:3px;font:7.5px "Arimo",sans-serif;padding-left:4px;color:#555}
.search-btn{width:18px;height:17px;background:var(--orange);border-radius:2px;display:flex;align-items:center;justify-content:center}
.ask{left:484px;top:7px;width:122px;height:34px}
.ask span{position:absolute;left:8px;top:4px;color:#fff;font-weight:700;font-size:14px}
.contact{left:487px;top:46px;font-size:8px;line-height:11px;color:var(--ink)}
.contact .tel{font-size:12.5px;font-weight:700;line-height:16px}
.contact .lbl{display:inline-block;width:30px}

/* nav */
.nav{left:111px;top:88px;width:546px;height:33px;display:flex;background:linear-gradient(#ff8a3a,var(--orange) 55%,var(--orange-dark));border-radius:2px 2px 0 0}
.nav a{flex:1;color:#fff;text-decoration:none;font-size:10.5px;display:flex;align-items:center;justify-content:center;border-right:1px solid rgba(0,0,0,.18);border-left:1px solid rgba(255,255,255,.2)}

/* hero */
.hero-band{left:0;top:121px;width:768px;height:244px;background:linear-gradient(#efefef,var(--band))}
.hero-frame{left:111px;top:121px;width:546px;height:265px;background:#fff;border-radius:0 0 6px 6px;box-shadow:0 6px 10px rgba(0,0,0,.12)}
.hero-photo{left:118px;top:128px;width:533px;height:248px;background:linear-gradient(100deg,#6a88c4 0%,#3b5aa8 40%,#1c2d66 65%,#7a5a3a 85%,#e0a050 100%)}
.hero-card{left:140px;top:142px;width:209px;height:190px;background:rgba(40,70,140,.72);color:#fff;padding:22px 14px}
.hero-card h1{font-size:12.5px;font-weight:400;text-align:center;line-height:15px;margin-bottom:16px}
.hero-card p{font-size:10px;line-height:12.5px}
.btn{display:inline-flex;align-items:center;justify-content:center;background:linear-gradient(var(--orange-light),var(--orange));color:#fff;font-weight:700;border-radius:3px;text-decoration:none}
.hero-btn{left:199px;top:319px;width:84px;height:24px;font-size:11px}
.arrow{width:34px;height:34px;border-radius:50%;background:#a9a9a9;top:235px;display:flex;align-items:center;justify-content:center}
.dots{left:370px;top:386px;display:flex;gap:2px}
.dots i{width:6px;height:6px;border-radius:50%;background:#aaa}
.dots i:first-child{background:var(--orange)}

/* intro */
.intro{left:122px;top:417px;width:525px;height:114px;background:#f5f5f5;border:1px solid var(--line);border-radius:3px;text-align:center;padding-top:27px}
.intro h2{font-size:16px;font-weight:700;color:#3a3a3a;margin-bottom:10px}
.intro p{font-size:9.5px;line-height:12.5px;color:#444;padding:0 30px}

/* roles */
.role{top:545px;width:127px;height:257px}
.role-head{height:29px;background:linear-gradient(var(--orange-light),var(--orange));border-radius:2px 2px 0 0;position:relative}
.role-head h3{position:absolute;left:12px;top:6px;font-size:13px;font-weight:700;color:#3a2a1a}
.role-head .notch{position:absolute;right:0;bottom:0}
.role-body{height:216px;background:linear-gradient(#ececec,#f8f8f8);border:1px solid var(--line);border-top:0;position:relative}
.role-body .hex{position:absolute;left:15px;top:12px}
.role-body p{position:absolute;left:8px;top:130px;width:112px;font-size:7.2px;line-height:9.3px;color:#444}
.more{position:absolute;right:6px;top:208px;width:56px;height:20px;font-size:7px;border-radius:10px;gap:5px}
.more svg{flex:none}

/* testimonials & newsletter */
.testi{left:122px;top:842px;width:333px;height:104px;background:var(--panel);border:1px solid var(--line);border-radius:3px}
.testi h4,.news h4{font-size:13.5px;font-weight:400;color:#333}
.testi h4{position:absolute;left:6px;top:6px}
.testi .portrait{position:absolute;left:18px;top:29px}
.testi blockquote{position:absolute;left:102px;top:31px;width:215px;font-size:8px;line-height:10px;color:#444}
.testi cite{position:absolute;left:102px;top:72px;font-size:8px;font-style:normal;color:#444}
.testi cite b{color:#d21d1d;font-weight:400}
.testi .nav-arrows{position:absolute;right:8px;bottom:6px}
.news{left:477px;top:842px;width:170px;height:104px;background:var(--panel);border:1px solid var(--line);border-radius:3px;overflow:hidden}
.news-head{height:28px;background:linear-gradient(#fafafa,#d8d8d8);padding:6px 8px}
.news p{font-size:8px;line-height:10px;text-align:center;color:#444;margin:9px 10px 0}
.news form{position:absolute;left:8px;top:67px;display:flex;gap:3px}
.news input{width:103px;height:18px;border:1px solid #999;font:7px "Arimo",sans-serif;padding-left:4px}
.news .btn{width:47px;height:18px;font-size:8px;font-weight:400;border-radius:1px;background:var(--orange)}

/* footer */
.footer{left:0;top:960px;width:768px;height:218px;background:var(--footer);color:#fff;font-size:7.5px}
.footer ul{list-style:none;position:absolute;top:8px;line-height:18px}
.footer .col{position:absolute;top:8px;line-height:13px}
.footer .col .head{margin-bottom:5px;line-height:18px}
.footer .col .gap{margin-top:12px}
.footer .col .gap-lg{margin-top:14px}
.social{display:flex;gap:4px;margin-top:7px}
.social i{width:24px;height:24px;border-radius:50%;background:#fff;display:block}
.copyright{left:0;top:1178px;width:768px;height:22px;background:var(--footer-deep);color:#fff;font-size:7.5px;text-align:center;line-height:22px}
</style>
</head>
<body>
<div class="page">

  <header>
    <div class="abs brand"><span class="brand-mark"></span><span class="brand-name">Velmar</span></div>
    <div class="abs search">
      <svg width="14" height="14" viewBox="0 0 14 14"><circle cx="8.5" cy="5.5" r="4" fill="none" stroke="#333" stroke-width="1.6"/><line x1="5.5" y1="8.5" x2="1.5" y2="12.5" stroke="#333" stroke-width="2"/></svg>
      <input type="text" value="Site Search" aria-label="Site search">
      <span class="search-btn"><svg width="7" height="7" viewBox="0 0 7 7"><path d="M0 0L7 3.5 0 7z" fill="#fff"/></svg></span>
    </div>
    <div class="abs ask">
      <svg width="122" height="40" viewBox="0 0 122 40"><path d="M2 2H120L114 28H78L72 38 70 28H2z" fill="var(--orange)"/></svg>
      <span>Any questions?</span>
    </div>
    <div class="abs contact">
      <div class="tel">Telp&nbsp;&nbsp;:+44 20 7946 0182</div>
      <div><span class="lbl">Fax</span>: +44 20 7946 0183</div>
      <div><span class="lbl">Email</span>: info@velmar.co.uk</div>
    </div>
  </header>

  <nav class="abs nav">
    <a href="#">HOME</a><a href="#">ABOUT US</a><a href="#">SERVICES</a><a href="#">PARTNERS</a><a href="#">CLIENTS</a><a href="#">CONTACT US</a>
  </nav>

  <section class="hero">
    <div class="abs hero-band"></div>
    <div class="abs hero-frame"></div>
    <div class="abs hero-photo" role="img" aria-label="Night view of illuminated glass office towers in a city financial district"></div>
    <div class="abs hero-card">
      <h1>YOU NEED INTEGRATION.<br>WE'RE INVICIBLE BUT ALWAYS SUPPORTING YOU.</h1>
      <p>Velmar is one of the leading systems integrators to the world's finance sector. We are an extension of your business and our services portfolio has been built so you have access to a complete partner.</p>
    </div>
    <a class="abs btn hero-btn" href="#">About Us</a>
    <span class="abs arrow" style="left:98px"><svg width="10" height="14" viewBox="0 0 10 14"><path d="M8 1L2 7l6 6" fill="none" stroke="#fff" stroke-width="2.5"/></svg></span>
    <span class="abs arrow" style="left:637px"><svg width="10" height="14" viewBox="0 0 10 14"><path d="M2 1l6 6-6 6" fill="none" stroke="#fff" stroke-width="2.5"/></svg></span>
    <div class="abs dots"><i></i><i></i><i></i><i></i></div>
  </section>

  <section class="abs intro">
    <h2>WHO ARE YOU?</h2>
    <p>If You are working financial organisation. We have the services to help anyone in your organisation work more efficiently productuively and more profitable.</p>
  </section>

  <section class="roles">
    <article class="abs role" style="left:122px">
      <div class="role-head"><h3>CEO</h3><svg class="notch" width="34" height="12"><path d="M10 0H34V12H0z" fill="#eee"/></svg></div>
      <div class="role-body">
        <svg class="hex" width="96" height="108" viewBox="0 0 96 108"><polygon points="48,2 94,28 94,80 48,106 2,80 2,28" fill="#fff" stroke="#bbb" stroke-width="2"/><polygon points="48,10 86,32 86,76 48,98 10,76 10,32" fill="#9aa4ad"/><polygon role="img" aria-label="Portrait of a chief executive in a suit" points="48,14 82,34 82,74 48,94 14,74 14,34" fill="#b9c4cc"/></svg>
        <p>Lorem ipsum dolor sit amet, consecteteur adipiscing elit. aenean comodo ligula eget dolor. aenean massa. cum sociis natoque penatibus et magnis disigula eget dolor. Aenean massa. Cum sociis natoque penatibus et...</p>
        <a class="btn more" href="#">Read more <svg width="5" height="6"><path d="M0 0l5 3-5 3z" fill="#fff"/></svg></a>
      </div>
    </article>
    <article class="abs role" style="left:254px">
      <div class="role-head"><h3>CFO</h3><svg class="notch" width="34" height="12"><path d="M10 0H34V12H0z" fill="#eee"/></svg></div>
      <div class="role-body">
        <svg class="hex" width="96" height="108" viewBox="0 0 96 108"><polygon points="48,2 94,28 94,80 48,106 2,80 2,28" fill="#fff" stroke="#bbb" stroke-width="2"/><polygon points="48,10 86,32 86,76 48,98 10,76 10,32" fill="#9aa4ad"/><polygon role="img" aria-label="Portrait of a finance director holding a tablet" points="48,14 82,34 82,74 48,94 14,74 14,34" fill="#6f7b86"/></svg>
        <p>Lorem ipsum dolor sit amet, consecteteur adipiscing elit. aenean comodo ligula eget dolor. aenean massa. cum sociis natoque penatibus et magnis disigula eget dolor. Aenean massa. Cum sociis natoque penatibus et...</p>
        <a class="btn more" href="#">Read more <svg width="5" height="6"><path d="M0 0l5 3-5 3z" fill="#fff"/></svg></a>
      </div>
    </article>
    <article class="abs role" style="left:387px">
      <div class="role-head"><h3>CTO</h3><svg class="notch" width="34" height="12"><path d="M10 0H34V12H0z" fill="#eee"/></svg></div>
      <div class="role-body">
        <svg class="hex" width="96" height="108" viewBox="0 0 96 108"><polygon points="48,2 94,28 94,80 48,106 2,80 2,28" fill="#fff" stroke="#bbb" stroke-width="2"/><polygon points="48,10 86,32 86,76 48,98 10,76 10,32" fill="#9aa4ad"/><polygon role="img" aria-label="Portrait of a technology director in a suit" points="48,14 82,34 82,74 48,94 14,74 14,34" fill="#c8cdd2"/></svg>
        <p>Lorem ipsum dolor sit amet, consecteteur adipiscing elit. aenean comodo ligula eget dolor. aenean massa. cum sociis natoque penatibus et magnis disigula eget dolor. Aenean massa. Cum sociis natoque penatibus et...</p>
        <a class="btn more" href="#">Read more <svg width="5" height="6"><path d="M0 0l5 3-5 3z" fill="#fff"/></svg></a>
      </div>
    </article>
    <article class="abs role" style="left:520px">
      <div class="role-head"><h3>Employee</h3><svg class="notch" width="34" height="12"><path d="M10 0H34V12H0z" fill="#eee"/></svg></div>
      <div class="role-body">
        <svg class="hex" width="96" height="108" viewBox="0 0 96 108"><polygon points="48,2 94,28 94,80 48,106 2,80 2,28" fill="#fff" stroke="#bbb" stroke-width="2"/><polygon points="48,10 86,32 86,76 48,98 10,76 10,32" fill="#9aa4ad"/><polygon role="img" aria-label="Group of office employees standing together" points="48,14 82,34 82,74 48,94 14,74 14,34" fill="#8a8fa8"/></svg>
        <p>Lorem ipsum dolor sit amet, consecteteur adipiscing elit. aenean comodo ligula eget dolor. aenean massa. cum sociis natoque penatibus et magnis disigula eget dolor. Aenean massa. Cum sociis natoque penatibus et...</p>
        <a class="btn more" href="#">Read more <svg width="5" height="6"><path d="M0 0l5 3-5 3z" fill="#fff"/></svg></a>
      </div>
    </article>
  </section>

  <section class="abs testi">
    <h4>Testimonials</h4>
    <svg class="portrait" width="66" height="66" viewBox="0 0 66 66"><circle cx="33" cy="33" r="32" fill="#fff" stroke="#ccc"/><circle role="img" aria-label="Portrait of a smiling client" cx="33" cy="33" r="27" fill="#b7aea6"/></svg>
    <blockquote>Lorem ipsum dolor sit amet, consectetuer adipiscing wlit. Sed diem nonumy inconvalls gravida reque. Nulla gravida vestibulum metis a acumsan, aliquam in sagitis ut.</blockquote>
    <cite><b>Peter Lanning</b>, California</cite>
    <svg class="nav-arrows" width="16" height="9" viewBox="0 0 16 9"><path d="M6 1L2 4.5 6 8M10 1l4 3.5L10 8" fill="none" stroke="#222" stroke-width="2"/></svg>
  </section>

  <section class="abs news">
    <div class="news-head"><h4>Newsletter</h4></div>
    <p>Receive Our Updates weekly, no worry about your details.</p>
    <form><input type="text" value="Email Address" aria-label="Email address"><a class="btn" href="#">SUBMIT</a></form>
  </section>

  <footer class="abs footer">
    <ul style="left:131px"><li>HOME</li><li>ABOUT US</li><li>SERVICES</li><li>PARTNERS</li><li>CLIENTS</li><li>CONTACT US</li></ul>
    <ul style="left:251px"><li>Sitemap</li><li>Help</li><li>Testimonials</li><li>Latest News</li><li>Privacy policy</li><li>Newsletter</li><li>Blog</li><li>Affiliates</li></ul>
    <div class="col" style="left:355px">
      <div class="head">LONDON OFFICE</div>
      <div>18 Halden Row,</div>
      <div>Mayfair, London&nbsp; W1K 2RT</div>
      <div>Telp.: +44 20 7946 0183</div>
      <div>W : info@velmar.co.uk</div>
      <div class="gap">SUPPORT;</div>
      <div>Telp.: +44 20 7946 0182</div>
      <div class="gap-lg">FOLLOW US ON:</div>
      <div class="social" aria-label="Social media links"><i></i><i></i><i></i><i></i></div>
    </div>
    <div class="col" style="left:500px">
      <div class="head">ESSEX OFFICE</div>
      <div>7 MARLOW WORKS, FENWICK LANE</div>
      <div>SOUTHEND, ESSEX SS2 4QW</div>
      <div>Telp.: +44 20 7946 0182</div>
      <div>W : info@velmar.co.uk</div>
      <div class="gap">SALES:</div>
      <div>Telp.: +44 20 7946 0182</div>
    </div>
  </footer>
  <div class="abs copyright">Copyright © 2015. Velmar.co.Uk. All rights reserved.</div>

</div>
</body>
</html>
```